Business Card & Stationary for Belmora Yards
1 sided business card and stationary
Modern
Trevor Hollis
WPMB Certified Applicator
48260 Pinecrest
Halden Falls, MO 64921
trevor@belmorayards.com
belmorayards.com
I like business cards that use the symbols for phone, web, and email rather than using the words.
I would also like to list my services on the card. They could all be listed on one line at the bottom of the card with bullets between them or wherever they may fit best with the rest of the design.
"Fertilization"
"Weed Control"
"Aeration"
"Verticutting"
"Seeding"
Should be plain white with nothing printed on it. (1 sided business card please)
Logo to use on card

```html
<!DOCTYPE html>
<html lang="en">
<head>
<meta charset="utf-8">
<title>Belmora Yards – Business Card</title>
<link rel="stylesheet" href="https://fonts.googleapis.com/css2?family=Open+Sans:ital,wght@0,400;0,600;0,700;1,700&display=swap">
<style>
  :root {
    --page-bg: #e6e6e4;
    --card-white: #ffffff;
    --brand-brown: #5a2414;
    --brand-green: #5e9b1d;
    --band-brown: #5b2515;
    --text-gray: #3d3d3d;
    --divider: #c9c9c9;
    --icon-green: #6aa62b;
  }
  * { box-sizing: border-box; margin: 0; padding: 0; }
  html, body {
    width: 1200px; height: 890px; overflow: hidden;
    background: var(--page-bg);
    font-family: "Open Sans", Arial, sans-serif;
  }
  .business-card {
    position: absolute; left: 100px; top: 159px;
    width: 1000px; height: 572px;
    background: var(--card-white);
    border-radius: 22px;
    overflow: hidden;
    box-shadow: 0 6px 22px rgba(0,0,0,0.18);
  }
  .brand-block {
    position: absolute; left: 30px; top: 150px; width: 420px; height: 180px;
    display: flex; align-items: center; justify-content: center; gap: 16px;
  }
  .brand-dot {
    width: 34px; height: 34px; border-radius: 50%;
    background: var(--brand-green); flex: none;
  }
  .brand-name {
    font-size: 50px; font-weight: 700; color: var(--brand-brown);
    line-height: 1; white-space: nowrap;
  }
  .divider {
    position: absolute; left: 470px; top: 62px; width: 2px; height: 300px;
    background: var(--divider);
  }
  .contact-block { position: absolute; left: 500px; top: 52px; }
  .person-name {
    font-size: 44px; font-weight: 700; color: var(--brand-brown); line-height: 1.1;
  }
  .person-title {
    font-size: 25px; font-weight: 700; color: var(--brand-green); margin-top: 2px;
  }
  .address {
    margin-top: 30px; font-size: 24px; color: var(--text-gray); line-height: 1.35;
  }
  .contact-list { list-style: none; margin-top: 28px; }
  .contact-list li {
    display: flex; align-items: center; gap: 14px;
    font-size: 24px; color: var(--text-gray); line-height: 1.45;
  }
  .contact-list svg { width: 24px; height: 24px; flex: none; }
  .bottom-band { position: absolute; left: 0; top: 0; width: 1000px; height: 572px; }
  .services {
    position: absolute; left: 0; right: 0; bottom: 38px;
    display: flex; justify-content: center; gap: 26px;
    list-style: none;
    color: #fff; font-size: 25px; font-weight: 700; font-style: italic;
  }
  .services li::before { content: "•"; margin-right: 10px; font-style: normal; }
</style>
</head>
<body>
  <div class="business-card">
    <svg class="bottom-band" viewBox="0 0 1000 572" aria-hidden="true">
      <path d="M0 445 Q500 400 1000 350 L1000 392 Q500 438 0 472 Z" fill="var(--brand-green)"/>
      <path d="M0 470 Q500 436 1000 390 L1000 572 L0 572 Z" fill="var(--band-brown)"/>
    </svg>

    <div class="brand-block">
      <span class="brand-dot"></span>
      <span class="brand-name">Belmora Yards</span>
    </div>

    <div class="divider"></div>

    <div class="contact-block">
      <div class="person-name">Trevor Hollis</div>
      <div class="person-title">WPMB Certified Applicator</div>
      <div class="address">48260 Pinecrest<br>Halden Falls, MO 64921</div>
      <ul class="contact-list">
        <li>
          <svg viewBox="0 0 24 24"><rect x="6" y="2" width="12" height="20" rx="2.5" fill="none" stroke="var(--icon-green)" stroke-width="2"/><rect x="9" y="5" width="6" height="8" fill="var(--icon-green)"/><circle cx="12" cy="18" r="1.5" fill="var(--icon-green)"/></svg>
          (555) 014-8273
        </li>
        <li>
          <svg viewBox="0 0 24 24"><circle cx="12" cy="12" r="4" fill="none" stroke="var(--icon-green)" stroke-width="2"/><path d="M16 8v5.5a2.5 2.5 0 0 0 5 0V12a9 9 0 1 0-3.5 7.1" fill="none" stroke="var(--icon-green)" stroke-width="2"/></svg>
          trevor@belmorayards.com
        </li>
        <li>
          <svg viewBox="0 0 24 24"><circle cx="12" cy="12" r="10" fill="none" stroke="var(--icon-green)" stroke-width="2"/><ellipse cx="12" cy="12" rx="4.5" ry="10" fill="none" stroke="var(--icon-green)" stroke-width="1.6"/><path d="M2 12h20M4 7h16M4 17h16" stroke="var(--icon-green)" stroke-width="1.4"/></svg>
          belmorayards.com
        </li>
      </ul>
    </div>

    <ul class="services">
      <li>Fertilization</li>
      <li>Weed Control</li>
      <li>Aeration</li>
      <li>Verticutting</li>
      <li>Seeding</li>
    </ul>
  </div>
</body>
</html>
```